Corporate Brightfen business cards to be handed to investor, bankers etc. Needs to have a young feel

I need business cards designed for a technology company that provides uber-like rapid response on the security industry. I would like it simple but very cool and tasteful. See attached documents for artwork and colours to be used. Cut sheet describes business model. Card stock should be thicker than normal. I would like the one side to be just the art and the other to have the contact info with maybe the pin somewhere.

Target Market(s)

Investors

Industry/Entity Type

Business

Contact Information for Business Card

Would like the logo attached on one side with name address and other info on the other side.

Font styles to use
Other font styles liked:
• See existing logo

Colors
6b449b
886aae
e4daeb
ffffff

Requirements
Must have
• Name: Dorian Felkatsis
• Address: 47 Larkfield Avenue, Toronto, On, M6K2B7
• Tel: 416-7291846
• Email: rolo@brightfen.io
Nice to have
• See logo colours

```html
<!DOCTYPE html>
<html lang="en">
<head>
<meta charset="utf-8">
<title>Brightfen Business Cards</title>
<link href="https://fonts.googleapis.com/css2?family=Exo+2:wght@400;500&display=swap" rel="stylesheet">
<style>
  :root {
    --violet-deep: #6b449b;
    --violet-mid: #886aae;
    --lilac: #cbb8dc;
    --lilac-pale: #e4daeb;
    --white: #ffffff;
    --stage: #ececec;
    --contact-text: #a48bc2;
  }
  * { margin: 0; padding: 0; box-sizing: border-box; }
  html, body { width: 1200px; height: 798px; overflow: hidden; }
  body {
    background: var(--stage);
    font-family: "Exo 2", sans-serif;
    position: relative;
  }
  .card {
    position: absolute;
    overflow: hidden;
    box-shadow: 0 10px 24px rgba(0,0,0,0.12);
  }
  /* Art side */
  .card-front {
    left: 190px; top: 154px;
    width: 280px; height: 490px;
    background: var(--lilac);
  }
  .card-front .brand-art {
    position: absolute; inset: 0;
    width: 100%; height: 100%;
  }
  .brand-name {
    position: absolute;
    left: 28px; bottom: 30px;
    font-weight: 500;
    font-size: 30px;
    line-height: 1;
    color: var(--white);
  }
  /* Contact side */
  .card-back {
    left: 520px; top: 259px;
    width: 490px; height: 280px;
    background: var(--white);
  }
  .card-back .contact-art {
    position: absolute; left: 0; top: 0;
    width: 490px; height: 280px;
  }
  .contact-block {
    position: absolute;
    left: 170px; top: 30px;
    right: 20px;
  }
  .person-name {
    font-weight: 500;
    font-size: 24px;
    color: var(--violet-deep);
    letter-spacing: 0.3px;
    margin-left: 8px;
  }
  .contact-list {
    list-style: none;
    margin-top: 30px;
    margin-left: 68px;
  }
  .contact-item {
    display: flex; align-items: flex-start; gap: 10px;
    font-weight: 400;
    font-size: 13px;
    line-height: 1.25;
    color: var(--contact-text);
    margin-bottom: 30px;
  }
  .contact-icon {
    flex: none;
    width: 14px; height: 14px;
    margin-top: 1px;
  }
</style>
</head>
<body>

<section class="card card-front" aria-label="Brightfen card, art side">
  <svg class="brand-art" viewBox="0 0 280 490" role="img" aria-label="Brand artwork: soft overlapping violet forms trailing down to a small point">
    <defs>
      <radialGradient id="artGlow" cx="0.72" cy="0.86" r="0.85">
        <stop offset="0" stop-color="#6b449b"/>
        <stop offset="0.35" stop-color="#886aae"/>
        <stop offset="0.75" stop-color="#b9a2d0"/>
        <stop offset="1" stop-color="#d6c6e3"/>
      </radialGradient>
    </defs>
    <rect width="280" height="490" fill="url(#artGlow)"/>
  </svg>
  <span class="brand-name">Brightfen</span>
</section>

<section class="card card-back" aria-label="Brightfen card, contact side">
  <svg class="contact-art" viewBox="0 0 490 280" role="img" aria-label="Brand artwork band in deep to soft violet tones">
    <defs>
      <linearGradient id="bandFill" x1="0" y1="0" x2="1" y2="1">
        <stop offset="0" stop-color="#6b449b"/>
        <stop offset="0.6" stop-color="#886aae"/>
        <stop offset="1" stop-color="#b9a2d0"/>
      </linearGradient>
    </defs>
    <path d="M0 0 H60 C120 60 150 170 250 280 H0 Z" fill="url(#bandFill)"/>
    <path d="M60 0 C120 60 150 170 250 280 H275 C175 170 140 70 85 0 Z" fill="#e4daeb"/>
  </svg>

  <div class="contact-block">
    <h1 class="person-name">Dorian Felkatsis</h1>
    <ul class="contact-list">
      <li class="contact-item">
        <svg class="contact-icon" viewBox="0 0 14 14" aria-hidden="true">
          <circle cx="7" cy="7" r="7" fill="var(--violet-mid)"/>
          <path d="M7 3.2a2.4 2.4 0 0 1 2.4 2.4C9.4 7.4 7 10.6 7 10.6S4.6 7.4 4.6 5.6A2.4 2.4 0 0 1 7 3.2z" fill="#fff"/>
          <circle cx="7" cy="5.6" r="0.9" fill="var(--violet-mid)"/>
        </svg>
        <span>47 Larkfield Avenue, Toronto,<br>On, M6K2B7</span>
      </li>
      <li class="contact-item">
        <svg class="contact-icon" viewBox="0 0 14 14" aria-hidden="true">
          <circle cx="7" cy="7" r="7" fill="var(--violet-mid)"/>
          <rect x="3.6" y="4.8" width="6.8" height="4.6" rx="0.6" fill="#fff"/>
          <path d="M3.8 5 L7 7.4 L10.2 5" fill="none" stroke="var(--violet-mid)" stroke-width="0.8"/>
        </svg>
        <span>rolo@brightfen.io</span>
      </li>
      <li class="contact-item">
        <svg class="contact-icon" viewBox="0 0 14 14" aria-hidden="true">
          <circle cx="7" cy="7" r="7" fill="var(--violet-mid)"/>
          <path d="M4.6 3.8l1.4-.2.7 1.7-.9.7a5 5 0 0 0 2.2 2.2l.7-.9 1.7.7-.2 1.4c-3.2.2-5.8-2.4-5.6-5.6z" fill="#fff"/>
        </svg>
        <span>416-7291846</span>
      </li>
    </ul>
  </div>
</section>

</body>
</html>
```